sailbuddies Website for children with diabilities

Hi, we are looking for a new website design for our community service "sailbuddies". Sailbuddies gives children who suffer from diseases or disabilities a week off on a Boat to give the children new hope and an unforgettable experience.

The current website is really old and we want to have a new one.
Please feel free to discover our website under http://sailbuddies-example.at/.
We have several company sponsors which are very important to us.

The Website has to be a Bootstrap Design (Version 4.4 or higher) [NOT Wordpress, Joomla, other CMS]

Target Market(s)

no target market. we like to inform our communities about our service.

Industry/Entity Type

community service for children with disabilities

Coding

Coded - Design and coding required

Number of Pages Required

4 page

Font styles to use
Sans Serif

Colors
0054AA
0677BA
7BADD7
CADEEF
E8F1F8
0094D4
00A9DD
6FCCEA
C7EBF8
E9F6FB

Requirements
Must have
• About, Sponsors, Information about cruises
Nice to have
• Gallery

```html
<!DOCTYPE html>
<html lang="en">
<head>
<meta charset="utf-8">
<title>Sailbuddies</title>
<link href="https://fonts.googleapis.com/css2?family=Exo+2:wght@500;600&family=Roboto:wght@400;500&display=swap" rel="stylesheet">
<style>
:root{
  --navy:#1b2470;
  --blue:#00a9dd;
  --blue-deep:#0094d4;
  --blue-soft:#6fccea;
  --ink:#111;
  --text:#3a3a3a;
  --muted:#9a9a9a;
  --white:#fff;
  --black:#000;
}
*{box-sizing:border-box;margin:0;padding:0}
html,body{width:1200px;height:3770px;overflow:hidden}
body{position:relative;background:var(--white);font-family:"Roboto",sans-serif;color:var(--text)}
.abs{position:absolute}
.head{font-family:"Exo 2",sans-serif;font-weight:500;color:var(--ink)}

.social-dot{position:absolute;top:21px;width:40px;height:40px;border-radius:50%;background:#c4c4c4}
.social-dot.on{background:var(--blue)}
.call-icon{left:829px;top:15px;width:44px;height:44px;border-radius:50%;background:var(--blue);display:flex;align-items:center;justify-content:center}
.call-label{left:882px;top:18px;font-size:12px;color:var(--blue-deep)}
.call-num{left:882px;top:36px;font-size:18px;color:var(--ink);font-weight:500}

.nav{left:111px;top:82px;width:978px;height:51px;background:var(--navy)}
.nav a{position:absolute;top:16px;color:var(--white);font-size:15px;font-weight:500;text-decoration:none;transform:translateX(-50%);white-space:nowrap}
.brand{left:520px;top:16px;width:146px;height:146px;border-radius:50%;background:var(--navy);border:4px solid var(--white);display:flex;align-items:center;justify-content:center;z-index:3}
.brand span{color:var(--white);font-family:"Exo 2",sans-serif;font-weight:600;font-size:20px}

.hero{left:0;top:108px;width:1200px;height:680px}
.hero-title{top:286px;width:1200px;text-align:center;font-family:"Exo 2",sans-serif;font-weight:600;font-size:47px;color:var(--white)}
.hero-sub{top:352px;left:300px;width:600px;text-align:center;font-size:14.5px;line-height:26px;color:var(--white)}

.btn{position:absolute;height:48px;border-radius:24px;display:flex;align-items:center;font-size:15px;font-weight:500;padding-left:6px}
.btn i{width:38px;height:38px;border-radius:50%;background:var(--white);margin-right:12px;display:block}
.btn.fill{background:var(--blue);color:var(--white);border:3px solid var(--white)}
.btn.fill i{border:3px solid var(--blue)}
.btn.line{background:var(--white);color:var(--blue);box-shadow:0 0 0 3px var(--blue) inset}
.btn.ghost{background:var(--white);color:var(--blue-deep);box-shadow:0 2px 6px rgba(0,0,0,.15)}
.btn.ghost i{background:#d9e4ea}

.section-title{width:1200px;text-align:center;font-size:35px}
.about-col{top:923px;font-size:14.5px;line-height:25.7px;color:var(--text)}

.goal{position:absolute}
.goal-panel{left:605px;top:1310px;width:595px;height:363px;background:linear-gradient(180deg,#22a8dc,#1c9fd3);color:var(--white);text-align:center}
.goal-panel h3{font-family:"Exo 2",sans-serif;font-weight:500;font-size:25px;line-height:36px;margin-top:56px}
.goal-panel hr{width:42px;border:0;border-top:3px solid var(--white);margin:14px auto 18px}
.goal-panel p{width:470px;margin:0 auto;font-size:14px;line-height:21px}

.tile{position:absolute;border-radius:8px;overflow:hidden}
.arrow{position:absolute;top:2121px;width:40px;height:40px;border-radius:50%;display:flex;align-items:center;justify-content:center}

.want-title{top:2816px;width:1200px;text-align:center;font-family:"Exo 2",sans-serif;font-weight:600;font-size:34px;color:var(--white)}
.want-text{top:2880px;left:90px;width:1020px;text-align:center;font-size:14.5px;line-height:30px;color:var(--white)}

.foot-h{top:3414px;font-family:"Exo 2",sans-serif;font-weight:500;font-size:22px;color:var(--white)}
.foot-h::after{content:"";display:block;width:32px;height:2px;background:var(--blue);margin-top:10px}
.foot-list{list-style:none;font-size:14.5px;color:var(--white)}
.foot-list li{height:30px;display:flex;align-items:center;gap:10px}
.field{position:absolute;left:847px;width:244px;border-bottom:1px solid #5a5a5a;font-size:14px;color:#cfcfcf;padding-bottom:12px}
.submit{left:847px;top:3588px;width:150px;height:40px;border-radius:20px;background:var(--blue);color:var(--white);font-size:15px;font-weight:500;display:flex;align-items:center;justify-content:center;box-shadow:0 0 12px rgba(0,169,221,.6)}
.rule{left:113px;top:3673px;width:978px;border-top:1px solid #1e1e1e}
.copy{top:3708px;width:1200px;text-align:center;font-size:14.5px;color:var(--white)}
</style>
</head>
<body>

<div class="social-dot on" style="left:112px"></div>
<div class="social-dot" style="left:160px"></div>
<div class="social-dot" style="left:207px"></div>
<div class="social-dot" style="left:255px"></div>

<div class="abs call-icon">
  <svg width="18" height="18" viewBox="0 0 24 24"><path fill="#fff" d="M6.6 10.8a15.1 15.1 0 0 0 6.6 6.6l2.2-2.2c.3-.3.7-.4 1-.2 1.1.4 2.3.6 3.6.6.6 0 1 .4 1 1V20c0 .6-.4 1-1 1A17 17 0 0 1 3 4c0-.6.4-1 1-1h3.5c.6 0 1 .4 1 1 0 1.3.2 2.5.6 3.6.1.3 0 .7-.2 1z"/></svg>
</div>
<div class="abs call-label">Call Us Today</div>
<div class="abs call-num">+1 555-010-0199</div>

<svg class="abs hero" viewBox="0 0 1200 680" role="img" aria-label="Sailboat anchored in a turquoise cove between rocky green cliffs">
  <defs>
    <linearGradient id="heroSky" x1="0" y1="0" x2="0" y2="1">
      <stop offset="0" stop-color="#7f9cbc"/>
      <stop offset=".35" stop-color="#6a7f5f"/>
      <stop offset=".6" stop-color="#3fa6a8"/>
      <stop offset="1" stop-color="#0f7f96"/>
    </linearGradient>
  </defs>
  <path d="M0 0H1200V447C1000 540 700 680 420 650 250 632 110 590 0 540Z" fill="url(#heroSky)"/>
  <path d="M0 540C110 590 250 632 420 650 700 680 1000 540 1200 447V462C1000 560 700 700 420 668 250 650 110 610 0 560Z" fill="#1ba3dc"/>
</svg>

<nav class="abs nav">
  <a style="left:106px">Home</a>
  <a style="left:205px">About</a>
  <a style="left:318px">Sponsors</a>
  <a style="left:691px">Information about cruises</a>
  <a style="left:867px">Gallery</a>
</nav>
<div class="abs brand"><span>sailbuddies</span></div>

<h1 class="abs hero-title">Verein Sailbuddies</h1>
<p class="abs hero-sub">Lorem ipsum dolor sit amet, consectetur adipiscing elit, sed do eiusmod tempor incididunt ut labore et dolore magna aliqua.</p>
<div class="btn fill" style="left:518px;top:420px;width:164px"><i></i>Get Started</div>

<h2 class="abs head section-title" style="top:850px">About Us</h2>
<p class="abs about-col" style="left:118px;width:470px">By experiencing a sailing week together, the "Sailbuddies fleet" creates ideal conditions under which the key objectives such as social integration and educational development of the children can be implemented in a concrete, efficient and professional manner and with a lasting effect.</p>
<p class="abs about-col" style="left:626px;width:460px">...trained social workers and experienced skippers who volunteer in the Sailbuddies association and organize a fleet for socially disadvantaged children and young people from central Upper Austria every year and set up the necessary financial resources.</p>
<div class="btn line" style="left:518px;top:1081px;width:164px"><i style="border:3px solid var(--blue)"></i>Learn More</div>

<h2 class="abs head section-title" style="top:1213px">Project Goals</h2>
<div class="goal" style="left:0;top:1310px;width:605px;height:363px;background:linear-gradient(180deg,#9fb8cc,#6d6e64 55%,#4d4a44)" role="img" aria-label="Group photo of children and skippers at the marina"></div>
<div class="goal goal-panel">
  <h3>Harbour Yacht Show goes<br>forth and multiplies!</h3>
  <hr>
  <p>Lorem ipsum dolor sit amet, consectetur adipiscing elit, sed do eiusmod tempor incididunt ut labore et dolore magna aliqua. Quis ipsum suspendisse ultrices gravida. Risus commodo viverra mae-</p>
  <div class="btn ghost" style="left:226px;top:252px;width:162px"><i></i>Learn More</div>
</div>
<div class="goal" style="left:0;top:1673px;width:605px;height:363px;background:linear-gradient(180deg,#5f9ad8,#3f78b5 50%,#1c5c9a)" role="img" aria-label="Sailing yacht with crew on open water"></div>
<div class="goal" style="left:605px;top:1673px;width:595px;height:363px;background:linear-gradient(180deg,#5a95d6,#4a7d4a 55%,#2668a6)" role="img" aria-label="Sailboat moored in a wooded bay"></div>

<h2 class="abs head" style="left:113px;top:2100px;font-size:33px">Our Gallery</h2>
<div class="abs" style="left:118px;top:2156px;font-size:15px;color:var(--muted)">Lorem ipsum dolor</div>
<div class="arrow" style="left:1000px;background:var(--blue)">
  <svg width="12" height="12" viewBox="0 0 12 12"><path d="M8 1 3 6l5 5" stroke="#fff" stroke-width="1.8" fill="none"/></svg>
</div>
<div class="arrow" style="left:1048px;background:#e3e3e3">
  <svg width="12" height="12" viewBox="0 0 12 12"><path d="m4 1 5 5-5 5" stroke="#555" stroke-width="1.8" fill="none"/></svg>
</div>

<div class="tile" style="left:111px;top:2226px;width:255px;height:206px;background:linear-gradient(160deg,#2f6f9a,#1e5a86)" role="img" aria-label="Child doing a handstand on a float"></div>
<div class="tile" style="left:111px;top:2444px;width:255px;height:205px;background:linear-gradient(160deg,#3a6b74,#6d5238)" role="img" aria-label="Children on the deck with a swim ring"></div>
<div class="tile" style="left:379px;top:2226px;width:316px;height:423px;background:linear-gradient(180deg,#8c8f8f,#4b8aa6 45%,#0fa6dc 80%,#00a9dd)" role="img" aria-label="Crew members relaxing aboard the boat">
  <div class="abs head" style="left:15px;top:355px;font-size:20px;color:var(--white)">Lorem Ipsum</div>
  <div class="abs" style="left:16px;top:390px;font-size:14px;color:var(--white)">Lorem Ipsum</div>
</div>
<div class="tile" style="left:707px;top:2226px;width:380px;height:206px;background:linear-gradient(180deg,#7aa4d6,#5c8fc8 55%,#2b67a6)" role="img" aria-label="Sailboat under full sail"></div>
<div class="tile" style="left:707px;top:2444px;width:158px;height:205px;background:linear-gradient(180deg,#3f77b3,#1d5590)" role="img" aria-label="Tube float on the sea"></div>
<div class="tile" style="left:874px;top:2444px;width:213px;height:205px;background:linear-gradient(180deg,#9ab8e0,#4a7fbd 60%,#1e4f8a)" role="img" aria-label="Sailboat on the horizon"></div>

<svg class="abs" style="left:0;top:2745px" width="1200" height="1025" viewBox="0 0 1200 1025" role="img" aria-label="Aerial view of a motor yacht on turquoise water">
  <defs>
    <linearGradient id="sea" x1="0" y1="0" x2="1" y2="1">
      <stop offset="0" stop-color="#1b8fc0"/>
      <stop offset=".6" stop-color="#1aa6d6"/>
      <stop offset="1" stop-color="#35b9e0"/>
    </linearGradient>
  </defs>
  <rect width="1200" height="1025" fill="#000"/>
  <path d="M0 0H1200V597C1080 520 960 460 820 445 600 420 300 500 0 670Z" fill="url(#sea)"/>
  <path d="M0 670C300 500 600 420 820 445 960 460 1080 520 1200 597V605C1080 530 960 470 820 455 600 432 300 512 0 682Z" fill="#fff"/>
</svg>
<h2 class="abs want-title">We Want...</h2>
<p class="abs want-text">...enabling children and young people who don't always have it easy in life to spend an unforgettable week in Croatia. It is precisely this shared experience that gives the children and young people a new zest for life and perspectives for their future. Through the reflection and also the care afterwards in the individual facilities, the children and young people can draw on this experience for a long time to come. This sustainability creates numerous pedagogical points of contact that represent a valuable basis for the achievement of goals.</p>
<div class="btn ghost" style="left:513px;top:3036px;width:164px"><i></i>Learn More</div>

<h3 class="abs foot-h" style="left:116px">Contact</h3>
<ul class="abs foot-list" style="left:116px;top:3470px">
  <li style="align-items:flex-start;height:56px;line-height:26px"><svg width="12" height="16" viewBox="0 0 12 16" style="margin-top:5px"><path d="M6 0a6 6 0 0 0-6 6c0 4.5 6 10 6 10s6-5.5 6-10a6 6 0 0 0-6-6zm0 8.5A2.5 2.5 0 1 1 6 3.5a2.5 2.5 0 0 1 0 5z" fill="#00a9dd"/></svg><span>Lorem ipsum dolor<br>sit amet</span></li>
  <li style="height:38px"><svg width="13" height="13" viewBox="0 0 24 24"><path fill="#00a9dd" d="M6.6 10.8a15.1 15.1 0 0 0 6.6 6.6l2.2-2.2c.3-.3.7-.4 1-.2 1.1.4 2.3.6 3.6.6.6 0 1 .4 1 1V20c0 .6-.4 1-1 1A17 17 0 0 1 3 4c0-.6.4-1 1-1h3.5c.6 0 1 .4 1 1 0 1.3.2 2.5.6 3.6.1.3 0 .7-.2 1z"/></svg>+1 555 010 0199</li>
  <li style="height:38px"><svg width="14" height="11" viewBox="0 0 14 11"><rect width="14" height="11" rx="1" fill="#00a9dd"/><path d="M0 1l7 5 7-5" stroke="#000" stroke-width="1.2" fill="none"/></svg>info@sailbuddies.com</li>
</ul>

<h3 class="abs foot-h" style="left:370px">Help Link</h3>
<ul class="abs foot-list" style="left:372px;top:3470px">
  <li><svg width="6" height="10" viewBox="0 0 6 10"><path d="m1 1 4 4-4 4" stroke="#fff" stroke-width="1.5" fill="none"/></svg>Terms &amp; conditions</li>
  <li><svg width="6" height="10" viewBox="0 0 6 10"><path d="m1 1 4 4-4 4" stroke="#fff" stroke-width="1.5" fill="none"/></svg>Privacy Policy</li>
  <li><svg width="6" height="10" viewBox="0 0 6 10"><path d="m1 1 4 4-4 4" stroke="#fff" stroke-width="1.5" fill="none"/></svg>About Us</li>
  <li><svg width="6" height="10" viewBox="0 0 6 10"><path d="m1 1 4 4-4 4" stroke="#fff" stroke-width="1.5" fill="none"/></svg>Support</li>
</ul>

<h3 class="abs foot-h" style="left:632px;top:3418px">Follow Us</h3>
<ul class="abs foot-list" style="left:632px;top:3467px">
  <li><i style="width:10px;height:10px;background:#fff;display:block"></i>Community</li>
  <li><i style="width:10px;height:10px;background:#fff;display:block"></i>Photo Feed</li>
  <li><i style="width:10px;height:10px;background:#fff;display:block"></i>News Feed</li>
  <li><i style="width:10px;height:10px;background:#fff;display:block"></i>Video Log</li>
</ul>

<h3 class="abs foot-h" style="left:846px">Newsletter Updates</h3>
<div class="field" style="top:3474px">Name*</div>
<div class="field" style="top:3526px">Email*</div>
<div class="abs submit">Submit Now</div>

<div class="abs rule"></div>
<div class="abs copy">© 2022 Sailbuddies &nbsp;All Rights Reserved</div>

</body>
</html>
```